Marketing fliers revised for 2024 Leap Onward

We are currently in the process of revitalizing our marketing fliers for the year 2024. Our leadership team has expressed their desire for a rejuvenated appearance for the upcoming year. In order to achieve this, we are seeking a different layout that effectively incorporates the same information.

To provide an example, the CEO has created a mock-up of the program, and I've attached the current flier, It is important to emphasize that we are aiming for a completely new and refreshed look.

This is our company website https://www.harborfinchdepot.com/

Target Market(s)

customers who buy roofing material

Industry/Entity Type

roofing and window

Colors
0054AA
0677BA
7BADD7
CADEEF
E8F1F8
0094D4
00A9DD
6FCCEA
C7EBF8
E9F6FB

Requirements
Must have
• all the details on the flier with a new look
Should not have
• the same look of he old flier

```html
<!DOCTYPE html>
<html lang="en">
<head>
<meta charset="utf-8">
<title>2024 Leap Onward Stay Aboard – HarborFinch Depot</title>
<link href="https://fonts.googleapis.com/css2?family=Montserrat:wght@500;700;800;900&display=swap" rel="stylesheet">
<style>
  :root{
    --navy:#0054AA;
    --blue:#0677BA;
    --sky:#7BADD7;
    --mist:#CADEEF;
    --ice:#E8F1F8;
    --cyan:#0094D4;
    --aqua:#00A9DD;
    --light-aqua:#6FCCEA;
    --white:#ffffff;
    --gold:#FFC20E;
    --orange:#F7941D;
    --backdrop:#e4e4e4;
  }
  *{box-sizing:border-box;margin:0;padding:0}
  html,body{width:1200px;height:1032px;overflow:hidden;background:var(--backdrop)}
  body{font-family:"Montserrat",sans-serif;color:var(--white)}
  .flyer{position:absolute;left:250px;top:26px;width:700px;height:980px;overflow:hidden;
    background:var(--navy);box-shadow:0 20px 40px rgba(0,0,0,.18)}
  .hero-photo{position:absolute;left:0;top:0;width:700px;height:600px;
    background:linear-gradient(180deg,var(--cyan) 0%,var(--sky) 35%,var(--mist) 55%,var(--blue) 100%)}
  .lower-field{position:absolute;left:0;top:600px;width:700px;height:380px;
    background:linear-gradient(160deg,var(--blue) 0%,var(--navy) 60%,#0a3f8e 100%)}
  .ribbon{position:absolute;left:40px;top:0;width:92px;height:112px;background:var(--orange);
    clip-path:polygon(0 0,100% 0,100% 100%,50% 86%,0 100%);
    display:flex;flex-direction:column;align-items:center;justify-content:center;padding-bottom:12px;
    font-weight:900;font-size:24px;line-height:1;text-align:center}
  .brand{position:absolute;right:30px;top:176px;display:flex;align-items:center;gap:8px;
    font-weight:800;font-size:15px;color:var(--navy);letter-spacing:.5px;white-space:nowrap}
  .brand-dot{width:16px;height:16px;border-radius:50%;background:var(--navy)}
  .headline{position:absolute;left:0;width:700px;text-align:center;font-weight:900;
    text-shadow:0 4px 10px rgba(0,40,100,.35)}
  .year{top:240px;font-size:200px;line-height:1;letter-spacing:-4px}
  .program{top:440px;font-size:66px;line-height:1;letter-spacing:1px}
  .band{position:absolute;left:0;top:572px;width:700px;height:52px;background:var(--aqua);
    display:flex;align-items:center;justify-content:center;font-weight:800;font-size:25px;letter-spacing:1px}
  .tier{position:absolute;width:140px;height:92px;border:1.5px solid var(--light-aqua);border-radius:6px;
    text-align:center;font-weight:800;line-height:1.05;padding-top:8px}
  .tier small{display:block;font-size:11px;letter-spacing:1px}
  .tier .amt{display:block;font-size:22px}
  .tier .get{display:block;font-size:20px}
  .stay-box{position:absolute;left:360px;top:644px;width:312px;height:192px;background:var(--aqua);
    padding:12px 14px;text-align:center;font-weight:900;
    display:flex;flex-direction:column;align-items:center;justify-content:center}
  .stay-box .title{font-size:32px;line-height:1;white-space:nowrap}
  .stay-box .sub{font-size:19px;font-weight:800;margin-top:6px;white-space:nowrap}
  .stay-box .bonus{font-size:68px;color:var(--gold);line-height:1;margin-top:6px;white-space:nowrap}
  .footer-frame{position:absolute;left:26px;top:852px;width:648px;height:112px;border:1.5px solid var(--white);
    display:flex;padding:12px 14px;gap:16px}
  .levels{width:250px;font-weight:800;font-size:13px;line-height:1.2}
  .levels .name{display:block;color:var(--gold);font-size:26px;font-weight:900}
  .levels .note{display:block;font-weight:500;font-size:12px;margin-top:2px}
  .invite{flex:1;font-size:13px;font-weight:800;line-height:1.2}
  .terms{font-size:8.5px;font-weight:500;line-height:1.3;margin-top:4px}
  .terms b{font-weight:800}
</style>
</head>
<body>
<main class="flyer">
  <div class="hero-photo" role="img" aria-label="Photo of two people leaping with arms raised against a misty blue sky"></div>
  <div class="lower-field"></div>

  <div class="ribbon"><span>IT'S</span><span>BACK!</span></div>

  <div class="brand"><span class="brand-dot"></span><span>HARBORFINCH DEPOT</span></div>

  <h1 class="headline year">2024</h1>
  <h2 class="headline program">LEAP ONWARD<br>STAY ABOARD</h2>

  <div class="band">NEW CUSTOMER RECEIVE UP TO $2,000</div>

  <div class="tier" style="left:30px;top:640px"><small>BUY</small><span class="amt">$10,000</span><small>RECEIVE</small><span class="get">$500</span></div>
  <div class="tier" style="left:190px;top:640px"><small>BUY</small><span class="amt">$25,000</span><small>RECEIVE</small><span class="get">$500</span></div>
  <div class="tier" style="left:30px;top:744px"><small>BUY</small><span class="amt">$50,000</span><small>RECEIVE</small><span class="get">$500</span></div>
  <div class="tier" style="left:190px;top:744px"><small>BUY</small><span class="amt">$150,000</span><small>RECEIVE</small><span class="get">$500</span></div>

  <section class="stay-box">
    <div class="title">STAY ABOARD</div>
    <div class="sub">RECEIVED ADDITIONAL</div>
    <div class="bonus">$1,000!</div>
  </section>

  <section class="footer-frame">
    <div class="levels">
      COMPLETE ALL LEVELS OF
      <span class="name">LEAP ONWARD</span>
      FOR AN ADDITIONAL $1000!
      <span class="note">JUST SPEND THE SAME OR MORE AS THE PREVIOUS YEAR</span>
    </div>
    <div class="invite">
      GIVE HARBORFINCH A TRY AND SEE WHAT OTHER CONTRACTORS HAVE DISCOVERED SINCE 1973
      <p class="terms"><b>Terms &amp; Conditions:</b> Rewards are issued as store credit after qualifying purchases post to a new account. Spend totals are measured per calendar year. Offer cannot be combined with other promotions and may change without notice. See branch staff for full details.</p>
    </div>
  </section>
</main>
</body>
</html>
```